Double-sided business card needed - specific brief

We need a double sided business card designed for our company Radiant Trimline. Having lost a lot of weight myself, the back of the card needs to show my before and after pictures. It needs to cover the entire back side of the card. This might be with my two before pictures over set on top of my main after picture or in separate frames. I'll leave that to your artistic consideration. The front needs to have our logo with contact details centred below.

The cards will be printed by PRINTKO.com and will be rectangular, 84mm x 55mm, but with ROUNDED edges. Please therefore present your designs rectangular but with rounded edges if possible.

The card should be designed in LANDSCAPE orientation.

As well as the logo, the front of the card should have the following details:

Moira Blakewell
Weight Loss Motivator with 189lb personal loss
moira@radiant-trimline.example
+44 (0)7700 900418

The website is important so should perhaps be more bold than the rest:
www.radiant-trimline.example

My brand colours are: Pink #CD2366, Light Pink #FD88AD. Blue #1C9CB1, Light Blue #64C4DE

Target Market(s)

Women 30+

Contact Information for Business Card

As description above

Font styles to use
Sans Serif

Requirements
Must have
• Double sided.
• Back side entirely covered with my before and after pictures.
• You may wish to float my before pictures on top of my after picture or add them in different frames. I look forward to seeing your different suggestions.

```html
<!DOCTYPE html>
<html lang="en">
<head>
<meta charset="utf-8">
<title>Radiant Trimline – Business Card</title>
<link href="https://fonts.googleapis.com/css2?family=Tinos:wght@400;700&display=swap" rel="stylesheet">
<style>
  :root {
    --pink: #CD2366;
    --light-pink: #FD88AD;
    --blue: #1C9CB1;
    --light-blue: #64C4DE;
    --white: #f4f1ee;
    --stage: #3a3a3c;
    --card-dark: #141416;
    --skin-light: #c49a82;
    --skin-mid: #8e6552;
    --hair-dark: #3e2520;
    --room-warm: #5a4a3e;
    --room-dark: #231f1d;
    --sofa: #6a4a36;
  }
  * { margin: 0; padding: 0; box-sizing: border-box; }
  html, body {
    width: 1200px; height: 896px; overflow: hidden;
    background: var(--stage);
    font-family: "Tinos", "Times New Roman", serif;
  }
  .sheet {
    width: 1200px; height: 896px;
    display: flex; align-items: center; justify-content: center; gap: 40px;
  }
  .card {
    position: relative;
    width: 540px; height: 354px;
    border-radius: 22px;
    overflow: hidden;
    box-shadow: 0 18px 40px rgba(0,0,0,.55);
  }

  /* Back: full-bleed before photo */
  .card--back { background: var(--hair-dark); }
  .back__photo {
    position: absolute; inset: 0;
    background:
      radial-gradient(ellipse 46% 58% at 38% 58%, var(--skin-light) 0%, var(--skin-mid) 55%, transparent 100%),
      linear-gradient(160deg, #5b2a26 0%, var(--hair-dark) 35%, #6e5346 100%);
  }
  .back__shade {
    position: absolute; top: 0; right: 0; bottom: 0; width: 52%;
    background: linear-gradient(90deg, rgba(20,14,12,0) 0%, rgba(20,14,12,.55) 45%, rgba(20,14,12,.7) 100%);
  }

  /* Front: dark card with after photo on the right */
  .card--front { background: var(--card-dark); }
  .front__photo {
    position: absolute; top: 0; right: 0; bottom: 0; width: 62%;
    background:
      radial-gradient(ellipse 40% 55% at 52% 42%, #b9a27a 0%, #6f5d48 50%, transparent 100%),
      radial-gradient(ellipse 60% 35% at 55% 92%, var(--sofa) 0%, transparent 100%),
      linear-gradient(135deg, var(--room-warm) 0%, var(--room-dark) 100%);
  }
  .front__fade {
    position: absolute; inset: 0;
    background:
      linear-gradient(90deg, var(--card-dark) 38%, rgba(20,20,22,.4) 62%, rgba(20,20,22,0) 80%),
      linear-gradient(0deg, rgba(20,20,22,.92) 0%, rgba(20,20,22,.6) 30%, rgba(20,20,22,0) 55%);
  }

  .brand {
    position: absolute;
    display: flex; align-items: center; gap: 10px;
  }
  .brand__dot {
    width: 20px; height: 20px; border-radius: 50%;
    background: var(--pink); flex: none;
  }
  .brand__name {
    color: var(--pink);
    font-weight: 400;
    text-transform: uppercase;
    letter-spacing: 1px;
    line-height: 1;
    white-space: nowrap;
  }
  .card--back .brand { top: 96px; right: 36px; }
  .card--back .brand__name { font-size: 28px; }
  .back__web {
    position: absolute; top: 140px; right: 36px;
    color: var(--white); font-size: 12px; letter-spacing: 1px;
  }
  .card--front .brand { left: 34px; top: 120px; }
  .card--front .brand__name { font-size: 30px; }
  .front__details { position: absolute; left: 34px; right: 30px; bottom: 26px; }
  .front__name {
    color: var(--light-blue); font-size: 24px; font-weight: 400; letter-spacing: 1.5px;
    text-transform: uppercase;
  }
  .front__role { color: var(--white); font-size: 13px; margin-top: 4px; }
  .front__rule { height: 1px; background: var(--white); margin: 10px 0 8px; opacity: .85; }
  .front__contact { color: var(--white); font-size: 11px; white-space: nowrap; }
  .front__contact .label { color: var(--light-blue); }
  .front__contact .web { font-weight: 700; }
</style>
</head>
<body>
<main class="sheet">
  <section class="card card--back">
    <div class="back__photo" role="img" aria-label="Before photo of the client, close-up portrait covering the whole back of the card"></div>
    <div class="back__shade"></div>
    <div class="brand">
      <span class="brand__dot"></span>
      <span class="brand__name">Radiant Trimline</span>
    </div>
    <p class="back__web">WWW.RADIANT-TRIMLINE.EXAMPLE</p>
  </section>

  <section class="card card--front">
    <div class="front__photo" role="img" aria-label="After photo of the client seated in a brown leather armchair in a warmly lit room"></div>
    <div class="front__fade"></div>
    <div class="brand">
      <span class="brand__dot"></span>
      <span class="brand__name">Radiant Trimline</span>
    </div>
    <div class="front__details">
      <h1 class="front__name">Moira Blakewell</h1>
      <p class="front__role">Weight Loss Motivator with 189lb personal loss</p>
      <div class="front__rule"></div>
      <p class="front__contact">
        <span class="label">P :</span> +44 (0)7700 900418
        <span class="label">| E :</span> moira@radiant-trimline.example
        <span class="label">| W :</span> <span class="web">www.radiant-trimline.example</span>
      </p>
    </div>
  </section>
</main>
</body>
</html>
```